Automotive eCommerce Business looking for a business card design

Looking for a clean and simple business card design. Our company name is "Harbor Crest Auto" and we are a company specializing in the ecommerce sales of automotive parts, specifically for pick up trucks and large SUVs. Our company colours are red, black, and white.

Feel free to use the logo provided or create a new logo that you seem fit. Looking forward to your creative ideas!

Industry/Entity Type

Automotive

Contact Information for Business Card

We were thinking of a possibly two-sided design featuring just the logo and company name on one side, and personal information on the other side. Single sided designs will be considered as well.

Font styles to use
Serif
Sans Serif
Decorative

Colors
ec1f27
ffffff
000000

Requirements
Must have
• Space for employee's name, title, phone number and email address, along with the company address and website somewhere.

```html
<!DOCTYPE html>
<html lang="en">
<head>
<meta charset="utf-8">
<title>Harbor Crest Auto – Business Card</title>
<link href="https://fonts.googleapis.com/css2?family=Cinzel:wght@400;500&family=Roboto:wght@400&family=Roboto+Condensed:wght@700&display=swap" rel="stylesheet">
<style>
  :root {
    --backdrop: #262626;
    --card-white: #f3f3f3;
    --brand-red: #9c1d22;
    --text-grey: #4a4a4a;
    --rule-grey: #8a8a8a;
    --white: #ffffff;
  }
  * { margin: 0; padding: 0; box-sizing: border-box; }
  html, body {
    width: 1200px; height: 960px; overflow: hidden;
    background: var(--backdrop);
  }
  .canvas { position: relative; width: 1200px; height: 960px; }

  .card {
    position: absolute; width: 600px; height: 343px;
    box-shadow: 0 2px 6px rgba(0,0,0,.5);
  }
  .card--front { left: 314px; top: 113px; background: var(--card-white); }
  .card--back { left: 311px; top: 472px; background: var(--brand-red); }

  /* front */
  .brand-mark {
    position: absolute; right: 34px; top: 154px;
    font-family: "Cinzel", serif; font-size: 17px; font-weight: 500;
    color: var(--text-grey); letter-spacing: .3px; white-space: nowrap;
  }
  .brand-square {
    position: absolute; left: 441px; top: 46px;
    width: 64px; height: 64px; background: var(--brand-red);
  }
  .name-tab {
    position: absolute; left: 0; top: 181px;
    width: 14px; height: 40px; background: var(--brand-red);
  }
  .person-name {
    position: absolute; left: 34px; top: 178px;
    font-family: "Roboto Condensed", sans-serif; font-weight: 700;
    font-size: 21px; color: var(--brand-red); line-height: 1;
  }
  .person-title {
    position: absolute; left: 35px; top: 206px;
    font-family: "Roboto", sans-serif; font-size: 14.5px;
    color: var(--text-grey); line-height: 1;
  }
  .divider {
    position: absolute; left: 34px; top: 230px;
    width: 529px; height: 1px; background: var(--rule-grey);
  }
  .contact-list {
    position: absolute; left: 35px; top: 240px; list-style: none;
    font-family: "Roboto", sans-serif; font-size: 14.5px; color: var(--text-grey);
  }
  .contact-list li {
    display: flex; align-items: center; height: 19px;
  }
  .contact-list svg { width: 14px; height: 14px; margin-right: 9px; fill: var(--brand-red); }
  .company-address {
    position: absolute; right: 36px; top: 257px; text-align: right;
    font-family: "Roboto", sans-serif; font-size: 14.5px;
    color: var(--text-grey); line-height: 19px; font-style: normal;
  }

  /* back */
  .back-name {
    position: absolute; right: 29px; top: 264px;
    font-family: "Cinzel", serif; font-size: 22px; font-weight: 400;
    color: var(--white); white-space: nowrap; line-height: 1;
  }
  .back-web {
    position: absolute; right: 29px; top: 291px;
    font-family: "Roboto", sans-serif; font-size: 13px;
    color: var(--white); letter-spacing: 4px; line-height: 1;
  }
</style>
</head>
<body>
<main class="canvas">
  <section class="card card--front" aria-label="Business card front">
    <div class="brand-square"></div>
    <div class="brand-mark">Harbor Crest Auto Ltd.</div>

    <div class="name-tab"></div>
    <h1 class="person-name">DANIEL REEVE</h1>
    <p class="person-title">CEO/FOUNDER</p>
    <div class="divider"></div>

    <ul class="contact-list">
      <li>
        <svg viewBox="0 0 16 16" aria-hidden="true"><path d="M3.2 1.5l2.4 2.6-1.3 1.8c.9 2 2.6 3.8 4.7 4.8l1.8-1.3 2.6 2.4-1.6 2.2C6.6 13.7 2.3 9.4 1 3.1z"/></svg>
        614 272 5809
      </li>
      <li>
        <svg viewBox="0 0 16 16" aria-hidden="true"><path d="M4 1h8v14H4zM5.5 2.5v9.5h5V2.5zM7.3 13h1.4v1.2H7.3z" fill-rule="evenodd"/></svg>
        742 315 6027
      </li>
      <li>
        <svg viewBox="0 0 16 16" aria-hidden="true"><path d="M4 1h8v4H4zM1 6h14v6h-2.5v-2h-9v2H1zM4.5 11h7v4h-7z"/></svg>
        519 604 3381
      </li>
      <li>
        <svg viewBox="0 0 16 16" aria-hidden="true"><path d="M1 4h14v9H1zM2 5l6 4.5L14 5v1.3L8 10.8 2 6.3z" fill-rule="evenodd"/></svg>
        dan@harborcrest.com
      </li>
    </ul>

    <address class="company-address">
      4218 Cedar Hollow Lane<br>
      Anchorage, Alaska 99507<br>
      www.harborcrest.com
    </address>
  </section>

  <section class="card card--back" aria-label="Business card back">
    <div class="back-name">HARBOR CREST AUTO LTD</div>
    <div class="back-web">www.harborcrest.com</div>
  </section>
</main>
</body>
</html>
```